Propose new minimalist design or Improve aesthetics of current one

Looking to create a minimalist clean business card, you can create your own concept using the elements we already have or improve on that one. Signature does not have to be used if a better idea is proposed.

Target Market(s)

Millennials, minimalist

Industry/Entity Type

REAL ESTATE

Contact Information for Business Card

Keep business card details

Colors

Designer to choose only greyscale colors for use in the design.

Requirements
Must have
• Keep business card details
Nice to have
• I like very minimalist fonts, nothing too busy
Should not have
• Curve designs or lines, colorful names, tacky home outlines

```html
<!DOCTYPE html>
<html lang="en">
<head>
<meta charset="utf-8">
<title>Lena Marlowe – Business Card</title>
<link rel="stylesheet" href="https://fonts.googleapis.com/css2?family=Montserrat:ital,wght@0,400;0,500;0,600;1,400&family=Playfair+Display:wght@400;700&display=swap">
<style>
  :root {
    --backdrop: #6e4a22;
    --card: #0b0b0b;
    --card-edge: #1c1c1c;
    --ink: #ffffff;
    --ink-soft: #e6e6e6;
    --photo-dark: #1a1614;
    --photo-mid: #5a4538;
    --photo-light: #b48e76;
    --signature-tone: #2a2a2a;
  }
  * { margin: 0; padding: 0; box-sizing: border-box; }
  html, body {
    width: 1200px;
    height: 1200px;
    overflow: hidden;
    background: var(--backdrop);
  }
  .stage {
    position: relative;
    width: 1200px;
    height: 1200px;
  }
  .card {
    position: absolute;
    width: 818px;
    height: 468px;
    background: radial-gradient(ellipse at 45% 30%, var(--card-edge) 0%, var(--card) 70%);
    color: var(--ink);
    overflow: hidden;
  }
  .card--front { left: 191px; top: 87px; }
  .card--back  { left: 194px; top: 582px; }

  /* Front */
  .brand {
    position: absolute;
    left: 0; right: 0;
    top: 118px;
    display: flex;
    justify-content: center;
    align-items: center;
    gap: 10px;
    font-family: "Montserrat", sans-serif;
    font-weight: 500;
    font-size: 15px;
    letter-spacing: 4px;
    text-transform: uppercase;
    color: var(--ink);
  }
  .brand__mark {
    width: 12px;
    height: 12px;
    border: 2px solid var(--ink);
  }
  .tagline {
    position: absolute;
    left: 0; right: 0;
    top: 228px;
    text-align: center;
    font-family: "Montserrat", sans-serif;
    font-style: italic;
    font-weight: 400;
    font-size: 27px;
    letter-spacing: 3.5px;
    color: var(--ink);
  }
  .signature {
    position: absolute;
    left: 302px;
    top: 300px;
    width: 214px;
    height: 95px;
    background: linear-gradient(90deg, var(--card) 0%, var(--signature-tone) 50%, var(--card) 100%);
  }

  /* Back */
  .portrait {
    position: absolute;
    left: 36px;
    top: 37px;
    width: 312px;
    height: 431px;
    background: radial-gradient(ellipse at 55% 35%, var(--photo-light) 0%, var(--photo-mid) 35%, var(--photo-dark) 75%, var(--card) 100%);
    border-radius: 140px 140px 0 0;
  }
  .details {
    position: absolute;
    left: 454px;
    top: 30px;
    font-family: "Montserrat", sans-serif;
    color: var(--ink-soft);
  }
  .name {
    font-family: "Playfair Display", serif;
    font-weight: 400;
    font-size: 38px;
    line-height: 1;
    color: var(--ink);
  }
  .name strong { font-weight: 700; }
  .role {
    margin-top: 8px;
    font-size: 15px;
    font-weight: 500;
    letter-spacing: 1px;
  }
  .contact {
    margin-top: 80px;
    list-style: none;
    font-size: 17px;
    line-height: 29px;
  }
  .contact b { font-weight: 600; margin-right: 4px; }
  .address {
    margin-top: 43px;
    font-size: 17px;
    line-height: 27px;
  }
  .social {
    margin-top: 41px;
    display: flex;
    align-items: center;
    gap: 10px;
    font-size: 17px;
    font-style: italic;
  }
  .social__dot {
    width: 14px;
    height: 14px;
    border: 2px solid var(--ink-soft);
    border-radius: 50%;
  }
</style>
</head>
<body>
<main class="stage">
  <section class="card card--front">
    <div class="brand"><span class="brand__mark"></span>Desert Lane Homes</div>
    <p class="tagline">Moving You Forward...</p>
    <div class="signature" role="img" aria-label="Handwritten signature of Lena Marlowe"></div>
  </section>

  <section class="card card--back">
    <div class="portrait" role="img" aria-label="Portrait photograph of the realtor in a black top"></div>
    <div class="details">
      <h1 class="name">Lena <strong>Marlowe</strong></h1>
      <p class="role">REALTOR</p>
      <ul class="contact">
        <li><b>P :</b>(555) 014 - 3826</li>
        <li><b>E :</b>lena@desertlanehomes.com</li>
        <li><b>W :</b>www.desertlanehomes.com</li>
      </ul>
      <p class="address">1200 North Mesa Avenue, Suite 210,<br>Sunvale, AZ 85000</p>
      <p class="social"><span class="social__dot"></span>@lenamarlowerealtor</p>
    </div>
  </section>
</main>
</body>
</html>
```